Orchard Bough Growing - Book Covers - Ebook, Paperback, Hardcover

Title would be:
Orchard Bough Growing
Subtitle: 7 Easy Stages Covering, Ground Choice, Blossom Care and Feeding, Trimming, Tiny Plots, Bug Management, Exotic Orchard Plants, and Vines
Author: Marlene Okafor
I would like the designer to have a couple of beautiful pictures on the cover. Please make it unique.
This would be posted on Quillora so please use specifications for book covers on Quillora
Back Cover should read:
Orchard Bough Growing
7 Easy Stages Covering, Ground Choice, Blossom Care and Feeding, Trimming, Tiny Plots, Bug Management, Exotic Orchard Plants, and Vines
Marlene Okafor
How to grow a thriving orchard and reap a bountiful harvest in less than a year – in both urban and non-urban settings
Fruit trees are fun to grow and will reward you with years of fresh, juicy homegrown produce.
However, the process can be excruciating, especially if you don’t know the best varieties to grow or how to control pests and diseases.
With a little planning and guidance, you will soon be biting into mellow fruits from trees in your backyard – including cherries, plums, pears, apples, and more.
All you need is to learn how to care for the trees, which you will find inside.
In Orchard Bough Growing, you’ll discover:
● How to pick the right fruit tree varieties for your growing zone and needs to ensure the plants don’t die
● How to effectively plan and prepare the planting site to lay a good foundation for your incoming trees
● How to choose the right irrigation system for your orchard and keep your fruit trees nourished all year long
● Examples of fruit garden plans for different regions – including a guide to help you design your small backyard space
● How to plant fruits to ensure proper pollination, fertilization, and flourishing growth of your produce
● Different fruit tree propagation methods with step-by-step instructions to help you grow your trees without spending money on costly grafts
● When and how to harvest fruits to ensure you collect them at their best and prevent wasting your hard work
● How to boost fruit production, encourage growth, and protect your trees from dangerous diseases
● How to look after fruit trees during all seasons, practice organic farming, and control pests in your garden
And much more…
It’s time to grow your mini-orchard and bask in years of harvest and sweetness from your labor.
Discover how you can have a thriving orchard and a bountiful fruit harvest.
Updates
Hello all Designers,
Please include this on the back cover as I forgot to include it in my main project:
Back Cover to read:
Orchard Bough Growing
Marlene Okafor
And much more…
Target Market(s)
People Who Love Gardening
Industry/Entity Type
Publishing
Requirements
Must have
- Title, Subtitle, Author Name, Beautiful Design, Eye Catching making you want to buy the book
Nice to have
- Large title, Easy to read subtitle intriguing pictures
Should not have
- Busy with too much stuff going on

```html
<!DOCTYPE html>
<html lang="en">
<head>
<meta charset="utf-8">
<title>Orchard Bough Growing – Book Cover</title>
<link href="https://fonts.googleapis.com/css2?family=Bebas+Neue&family=Montserrat:wght@700&family=Open+Sans:ital,wght@0,400;1,400&display=swap" rel="stylesheet">
<style>
  :root {
    --leaf: #8dc63f;
    --forest: #00733a;
    --sky: #a6dcf2;
    --sky-light: #cdeaf6;
    --paper: #ffffff;
    --ink: #1c2a22;
    --backdrop: #eeeeee;
  }
  * { margin: 0; padding: 0; box-sizing: border-box; }
  html, body {
    width: 1059px; height: 1200px; overflow: hidden;
    background: var(--backdrop);
  }
  .cover {
    position: absolute; left: 29px; top: 242px;
    width: 1000px; height: 716px;
    background: var(--forest);
    box-shadow: 0 6px 18px rgba(0,0,0,.25);
    overflow: hidden;
  }
  /* bottom bands */
  .base-line {
    position: absolute; left: 0; top: 631px; width: 1000px; height: 9px;
    background: var(--leaf);
  }
  .base-band {
    position: absolute; left: 0; top: 640px; width: 1000px; height: 76px;
    background: var(--forest);
  }
  .code-box {
    position: absolute; left: 297px; top: 602px; width: 160px; height: 92px;
    background: var(--paper);
  }

  /* back cover */
  .back { position: absolute; left: 0; top: 0; width: 478px; height: 631px; }
  .back-head {
    height: 70px; background: var(--leaf);
    display: flex; align-items: center; justify-content: center;
  }
  .back-title {
    font-family: "Bebas Neue", sans-serif; font-weight: 400;
    font-size: 56px; line-height: 1; color: var(--paper);
    letter-spacing: 1px; padding-top: 4px;
  }
  .back-body {
    height: 561px;
    background: linear-gradient(100deg, var(--sky-light) 0%, var(--sky) 100%);
    padding: 43px 24px 0 17px;
    font-family: "Open Sans", sans-serif; font-size: 9.4px; line-height: 1.18;
    color: var(--ink);
  }
  .back-intro { margin-bottom: 10px; }
  .discover-list { list-style: none; text-align: center; font-style: italic; }
  .discover-list li { margin: 0 auto 10px; max-width: 300px; }
  .discover-list li::before { content: "\25CF\00a0"; font-style: normal; }
  .discover-list li.wide { max-width: 380px; }
  .back-close { margin-top: 2px; }

  /* spine */
  .spine {
    position: absolute; left: 478px; top: 0; width: 44px; height: 631px;
    background: var(--leaf);
  }
  .spine-title, .spine-author {
    position: absolute; left: 50%; writing-mode: vertical-rl;
    transform: translateX(-50%); color: var(--forest); white-space: nowrap;
  }
  .spine-title {
    top: 14px; font-family: "Bebas Neue", sans-serif; font-size: 27px; line-height: 1;
  }
  .spine-author {
    top: 450px; font-family: "Montserrat", sans-serif; font-weight: 700; font-size: 15px;
  }

  /* front cover */
  .front { position: absolute; left: 522px; top: 0; width: 478px; height: 631px; }
  .front-head {
    height: 70px; background: var(--leaf);
    display: flex; align-items: center; justify-content: center; text-align: center;
    font-family: "Bebas Neue", sans-serif; font-size: 17.5px; line-height: 1.07;
    color: var(--paper); padding: 4px 14px 0;
  }
  .front-body {
    position: relative; height: 561px;
    background: linear-gradient(75deg, var(--sky) 0%, var(--sky-light) 45%, var(--paper) 100%);
  }
  .front-title {
    position: absolute; left: 0; right: 0; top: 20px; text-align: center;
    font-family: "Bebas Neue", sans-serif; font-weight: 400; line-height: .86;
  }
  .front-title .line-light { display: block; font-size: 80px; color: var(--leaf); }
  .front-title .line-dark { display: block; font-size: 122px; color: var(--forest); }
  .fruit-photo {
    position: absolute; left: 0; right: 0; top: 180px; bottom: 0;
    background:
      radial-gradient(ellipse 30% 40% at 90% 80%, rgba(196,52,40,.85), transparent 70%),
      radial-gradient(ellipse 22% 55% at 62% 62%, rgba(214,160,40,.9), transparent 72%),
      radial-gradient(ellipse 25% 40% at 40% 82%, rgba(245,204,60,.9), transparent 70%),
      radial-gradient(ellipse 18% 26% at 18% 72%, rgba(212,50,100,.8), transparent 72%),
      radial-gradient(ellipse 30% 30% at 20% 30%, rgba(120,190,60,.45), transparent 75%);
  }
  .front-author {
    position: absolute; left: 522px; top: 640px; width: 478px; height: 76px;
    display: flex; align-items: center; justify-content: center;
    font-family: "Montserrat", sans-serif; font-weight: 700; font-size: 24px;
    color: var(--paper);
  }
</style>
</head>
<body>
  <div class="cover">
    <section class="back">
      <header class="back-head"><h2 class="back-title">ORCHARD BOUGH GROWING</h2></header>
      <div class="back-body">
        <p class="back-intro">Orchard Bough Growing 7 Easy Stages Covering, Ground Choice, Blossom Care and Feeding, Trimming, Tiny Plots, Bug Management, Exotic Orchard Plants, and Vines Marlene Okafor How to grow a thriving orchard and reap a bountiful harvest in less than a year – in both urban and non-urban settings Fruit trees are fun to grow and will reward you with years of fresh, juicy homegrown produce. However, the process can be excruciating, especially if you don’t know the best varieties to grow or how to control pests and diseases. With a little planning and guidance, you will soon be biting into mellow fruits from trees in your backyard – including cherries, plums, pears, apples, and more. All you need is to learn how to care for the trees, which you will find inside. In Orchard Bough Growing, you’ll discover:</p>
        <ul class="discover-list">
          <li>How to pick the right fruit tree varieties for your growing zone and needs to ensure the plants don’t die</li>
          <li>How to effectively plan and prepare the planting site to lay a good foundation for your incoming trees</li>
          <li>How to choose the right irrigation system for your orchard and keep your fruit trees nourished all year long</li>
          <li>Examples of fruit garden plans for different regions – including a guide to help you design your small backyard space</li>
          <li>How to plant fruits to ensure proper pollination, fertilization, and flourishing growth of your produce</li>
          <li class="wide">Different fruit tree propagation methods with step-by-step instructions to help you grow your trees without spending money on costly grafts</li>
          <li>When and how to harvest fruits to ensure you collect them at their best and prevent wasting your hard work</li>
          <li>How to boost fruit production, encourage growth, and protect your trees from dangerous diseases</li>
          <li>How to look after fruit trees during all seasons, practice organic farming, and control pests in your garden And much more…</li>
        </ul>
        <p class="back-close">It’s time to grow your mini-orchard and bask in years of harvest and sweetness from your labor. Discover how you can have a thriving orchard and a bountiful fruit harvest.</p>
      </div>
    </section>

    <aside class="spine">
      <span class="spine-title">ORCHARD BOUGH GROWING</span>
      <span class="spine-author">Marlene Okafor</span>
    </aside>

    <section class="front">
      <header class="front-head">
        <p>7 Easy Stages Covering, Ground Choice, Blossom Care and Feeding, Trimming, Tiny Plots, Bug Management, Exotic Orchard Plants, and Vines</p>
      </header>
      <div class="front-body">
        <div class="fruit-photo" role="img" aria-label="Photograph of tropical fruits: a child's hands holding a dragon fruit beside bananas, a pineapple, mangoes and a fruiting branch"></div>
        <h1 class="front-title">
          <span class="line-light">ORCHARD BOUGH</span>
          <span class="line-dark">GROWING</span>
        </h1>
      </div>
    </section>

    <div class="base-line"></div>
    <div class="base-band"></div>
    <div class="code-box"></div>
    <p class="front-author">Marlene Okafor</p>
  </div>
</body>
</html>
```